Anzeigengestaltung Zeitung für eine Zahnarztpraxis
Zielgruppe
Zahnarztpraxis, spezialisiert auf hochwertige Zahnbehandlungen.
Aufgabenstellung
Ziel soll es sein Patienten mit Zahnarztangst zu motivieren einen Ersttermin zu vereinbaren
Ganzseitige Anzeige, im Format Breite 192 mm x 290 mm.
Die Anzeige sollte sympathisch, kreativ rüberkommen um Kontaktängste abzubauen.
Es sollte ein Foto von mir als Hauptbehandler verwendet werden, es können jedoch zusätzlich auch stock Fotos dazu genommen werden. Frauen als auch Männer sollten angesprochen werden.
Kontaktangaben in der Anzeige:
Dentivera MVZ, Dr. med. dent. Lukas Brenner & Kollegen
Weidenhofer Str. 17
68519 Lampertheim
www.dentivera-beispiel.de
Tel.: 06206 5917
Email: kontakt@dentivera-beispiel.de

```html
<!DOCTYPE html>
<html lang="de">
<head>
<meta charset="utf-8">
<title>Dentivera – Zeitungsanzeige</title>
<link href="https://fonts.googleapis.com/css2?family=Montserrat:wght@300;400;500;600;700&display=swap" rel="stylesheet">
<style>
  :root{
    --page-bg:#e9e9eb;
    --paper:#f4f4f4;
    --ink:#2f2f33;
    --copper:#b8743a;
    --band:#3c3c40;
    --band-dark:#2c2c30;
    --navy:#2f3d70;
    --gold-ring:#c9a86a;
    --label:#ffffff;
    --badge-red:#d8262f;
  }
  *{box-sizing:border-box;margin:0;padding:0}
  html,body{width:1200px;height:900px;overflow:hidden;background:var(--page-bg);font-family:"Montserrat",sans-serif;color:var(--ink)}
  .ad{position:absolute;left:313px;top:17px;width:574px;height:866px;background:var(--paper);overflow:hidden;box-shadow:0 8px 24px rgba(0,0,0,.12)}
  .headline{position:absolute;left:36px;top:38px;font-size:30px;line-height:1.12;font-weight:700;letter-spacing:-.3px;color:var(--ink);z-index:3}
  .headline .accent{color:var(--copper)}
  .brand{position:absolute;right:38px;top:178px;text-align:right;color:var(--copper);z-index:3;display:flex;align-items:center;gap:10px}
  .brand-mark{width:14px;height:14px;border-radius:50%;background:var(--copper)}
  .brand-name{font-size:22px;font-weight:500;letter-spacing:4px;line-height:1}
  .brand-sub{display:block;font-size:9px;letter-spacing:4px;margin-top:4px}
  .hero-photo{position:absolute;left:0;top:150px;width:574px;height:370px;
    background:radial-gradient(ellipse at 62% 50%,#c9ccd6 0%,#dfe1e7 40%,rgba(244,244,244,0) 72%),
               radial-gradient(ellipse at 25% 35%,#e8e3da 0%,rgba(244,244,244,0) 55%);}
  .intro{position:absolute;left:36px;top:474px;width:515px;font-size:12px;line-height:1.45;font-weight:500;color:var(--ink);z-index:3}
  .focus-band{position:absolute;left:0;top:560px;width:574px;height:165px;background:linear-gradient(180deg,var(--band) 0%,var(--band-dark) 100%)}
  .focus-title{position:absolute;left:28px;top:572px;font-size:20px;font-weight:300;line-height:1.15;color:var(--label);letter-spacing:1px;z-index:3}
  .focus-title strong{display:inline-block;font-weight:600;background:var(--copper);padding:0 6px;margin-left:-6px}
  .focus-list{position:absolute;left:212px;top:600px;width:350px;display:flex;justify-content:space-between;list-style:none;z-index:3}
  .focus-item{width:84px;text-align:center;color:var(--label);font-size:9px;font-weight:600;line-height:1.2;letter-spacing:.3px}
  .focus-icon{display:block;width:62px;height:62px;margin:0 auto 8px}
  .portrait{position:absolute;left:18px;top:646px;width:180px;height:220px;z-index:2;
    background:linear-gradient(180deg,#ece6df 0%,#d9c3ad 35%,#3d4a80 62%,var(--navy) 100%)}
  .contact{position:absolute;left:230px;top:735px;font-size:11.5px;line-height:1.4;color:var(--ink);z-index:3;font-style:normal}
  .contact .org{color:var(--copper);font-weight:600}
  .contact .lead{font-weight:700}
  .contact .key{color:var(--copper)}
  .badges{position:absolute;left:230px;top:838px;display:flex;gap:14px;align-items:center}
  .badge-rating{width:96px;height:24px;background:#dfe3e6;border-left:20px solid #4a9ec9}
  .badge-listing{width:84px;height:20px;background:var(--badge-red)}
</style>
</head>
<body>
<main class="ad">
  <h1 class="headline">Suchen Sie einen<br><span class="accent">Zahnarzt</span> in<br>Lampertheim?</h1>

  <div class="hero-photo" role="img" aria-label="Foto: Zahnarzt im Gespräch mit einem älteren Patienten vor einem Bildschirm mit Röntgenaufnahme"></div>

  <div class="brand">
    <span class="brand-mark"></span>
    <div><span class="brand-name">Dentivera</span><span class="brand-sub">Lampertheim</span></div>
  </div>

  <p class="intro">In unserem modernen zahnärztlichen Versorgungszentrum befindet sich die gesamte Zahnmedizin unter einem Dach. Hier erwarten Sie Experten, die Ihnen in allen Bereichen der Zahnmedizin mit neuester Technik und bestmöglichen Behandlungsmethoden eine angstfreie Behandlung ermöglichen.</p>

  <section class="focus-band" aria-label="Schwerpunkte"></section>
  <h2 class="focus-title">UNSERE<br><strong>SCHWERPUNKTE</strong><br>SIND:</h2>

  <ul class="focus-list">
    <li class="focus-item">
      <svg class="focus-icon" viewBox="0 0 62 62"><circle cx="31" cy="31" r="29" fill="var(--navy)" stroke="var(--gold-ring)" stroke-width="2"/><path d="M22 20c4-3 14-3 18 0 2 2 1 6-1 8H23c-2-2-3-6-1-8z" fill="#fff"/><rect x="27" y="30" width="8" height="14" rx="1" fill="#d6d9e2"/><path d="M26 33h10M26 37h10M26 41h10" stroke="#9aa0b5" stroke-width="1.2"/></svg>
      ZAHNIM-<br>PLANTATE
    </li>
    <li class="focus-item">
      <svg class="focus-icon" viewBox="0 0 62 62"><circle cx="31" cy="31" r="29" fill="var(--navy)" stroke="var(--gold-ring)" stroke-width="2"/><rect x="16" y="19" width="30" height="20" rx="2" fill="none" stroke="#fff" stroke-width="2"/><rect x="20" y="23" width="22" height="12" fill="#d6d9e2"/><path d="M27 43h8M31 39v4" stroke="#fff" stroke-width="2"/></svg>
      DIGITALER ZAH-<br>NERSATZ
    </li>
    <li class="focus-item">
      <svg class="focus-icon" viewBox="0 0 62 62"><circle cx="31" cy="31" r="29" fill="var(--navy)" stroke="var(--gold-ring)" stroke-width="2"/><path d="M14 31h34" stroke="#fff" stroke-width="2"/><rect x="16" y="26" width="7" height="10" rx="2" fill="#fff"/><rect x="24.5" y="26" width="7" height="10" rx="2" fill="#fff"/><rect x="33" y="26" width="7" height="10" rx="2" fill="#fff"/><rect x="41.5" y="26" width="5" height="10" rx="2" fill="#fff"/></svg>
      KIEFER-<br>ORTHOPÄDIE
    </li>
    <li class="focus-item">
      <svg class="focus-icon" viewBox="0 0 62 62"><circle cx="31" cy="31" r="29" fill="var(--navy)" stroke="var(--gold-ring)" stroke-width="2"/><path d="M20 22c3-4 8-3 11-1 3-2 8-3 11 1 2 4 0 9-2 13l-2 10c-1 2-3 2-3 0l-2-8c-1-2-3-2-4 0l-2 8c0 2-2 2-3 0l-2-10c-2-4-4-9-2-13z" fill="#fff"/><path d="M25 31l4 4 8-8" fill="none" stroke="var(--navy)" stroke-width="2.4"/></svg>
      WURZELBE-<br>HANDLUNG
    </li>
  </ul>

  <div class="portrait" role="img" aria-label="Foto: lächelnder Hauptbehandler in dunkelblauer Praxiskleidung"></div>

  <address class="contact">
    <span class="org">Dentivera MVZ</span><br>
    <span class="lead">Dr. med. dent. Lukas Brenner &amp; Kollegen</span><br>
    Weidenhofer Str. 17 68519 Lampertheim<br>
    <span class="key">Tel.:</span> 06206 5917<br>
    <span class="key">Email:</span> kontakt@dentivera-beispiel.de<br>
    <span class="key">Web :</span> www.dentivera-beispiel.de
  </address>

  <div class="badges">
    <span class="badge-rating" role="img" aria-label="Bewertungssiegel"></span>
    <span class="badge-listing" role="img" aria-label="Auszeichnungssiegel eines Gesundheitsmagazins"></span>
  </div>
</main>
</body>
</html>
```